Club Lumora - Dermatology Consultation App

Club Lumora is launching a new Quince QWS App for online Dermatology consultation. We would appreciate a simple Scandinavian design which communicates trust, comfort and expensive feel. Most yacht designs have similar color palette, light wood colors and textures, but don’t be restricted by those in your artistic search.
The process is completed in three easy steps:
1. take a Snapshot.
2. Describe and Send it.
3. get Diagnosis and Treatment.
The Home screen should also have buttons - Start new Case, Follow up Visit, Rx Refill.
15% of the Home screen should also have a field/button - Medical Cosmetics Shop.
10% of the Home screen should also have a field or buttons for Our Partners (sponsors) – Talvine, Norelisa, Parlo, Ostra. (if you click you would be directed to their sites)
Note / Suggestion : Maybe you could use a larger picture of a dermatologist and have overlying fields and content, just for more influencing effect. (I am not a professional though)
Thank you so much.
Updates
Target Market(s)
24 - 59 Female
Industry/Entity Type
Club
Look and feel

```html
<!DOCTYPE html>
<html lang="en">
<head>
<meta charset="utf-8">
<title>Club Lumora – Three Steps</title>
<link href="https://fonts.googleapis.com/css2?family=Raleway:wght@300;400;500&display=swap" rel="stylesheet">
<style>
  :root {
    --brand: #c0876c;
    --ink: #5a5a5a;
    --name-ink: #6a6a6a;
    --rule: #c9c9c9;
    --paper: #ffffff;
    --frame: #d6d6d6;
    --on-photo: #f3e6de;
    --skin-dark: #6e4330;
    --skin-mid: #a8704f;
    --skin-light: #d2a088;
  }
  * { box-sizing: border-box; margin: 0; padding: 0; }
  html, body { width: 1200px; height: 1000px; overflow: hidden; background: var(--paper); }
  body { font-family: "Raleway", sans-serif; color: var(--ink); }

  .canvas {
    position: relative; width: 1200px; height: 1000px;
    border: 1px solid var(--frame); background: var(--paper);
  }
  .brand-title {
    position: absolute; top: 22px; left: 0; width: 100%;
    text-align: center; font-weight: 300; font-size: 30px;
    text-transform: uppercase; letter-spacing: 8px; color: var(--name-ink);
  }

  .screen {
    position: absolute; background: var(--paper); border: 1px solid #2b2b2b; overflow: hidden;
  }
  .screen--describe { left: 115px; top: 130px; width: 250px; height: 665px; }
  .screen--snapshot { left: 430px; top: 198px; width: 338px; height: 597px; }
  .screen--result { left: 835px; top: 130px; width: 253px; height: 670px; }

  .app-header {
    position: relative; height: 62px; border-bottom: 2px solid var(--brand);
  }
  .screen--result .app-header { height: 118px; }
  .app-name {
    position: absolute; bottom: 12px; left: 14px;
    font-size: 15px; font-weight: 400; text-transform: uppercase; letter-spacing: 3px;
    color: var(--name-ink);
  }
  .menu-icon { position: absolute; bottom: 14px; right: 12px; width: 20px; height: 18px; }
  .screen--result .menu-icon { top: 28px; bottom: auto; }

  .partners {
    position: relative; display: flex; justify-content: space-around;
    padding: 8px 4px 0; font-size: 14px; color: var(--ink);
  }

  .skin-photo {
    background: linear-gradient(160deg, var(--skin-light) 0%, var(--skin-mid) 45%, var(--skin-dark) 70%, var(--skin-mid) 100%);
  }
  .describe-photo { margin: 14px 10px 0; height: 262px; }

  .describe-field { margin: 16px 6px 0; }
  .describe-label {
    font-size: 16px; color: var(--ink); border-left: 2px solid #8cc4d3;
    padding-left: 4px; padding-bottom: 4px; border-bottom: 1px solid var(--rule);
  }
  .describe-line { height: 26px; border-bottom: 1px solid var(--rule); }

  .actions {
    position: absolute; bottom: 12px; left: 0; width: 100%;
    display: flex; justify-content: center; gap: 30px;
  }
  .action { text-align: center; font-size: 10px; color: var(--ink); }
  .action-button {
    width: 54px; height: 54px; border-radius: 50%; background: var(--brand);
    display: flex; align-items: center; justify-content: center; margin: 0 auto 4px;
  }

  /* snapshot screen */
  .screen--snapshot .app-header { border-bottom: 1px solid rgba(255,255,255,0.7); }
  .screen--snapshot .app-name, .screen--snapshot .partners { color: var(--on-photo); }
  .camera-view { position: absolute; inset: 0; }
  .viewfinder { position: absolute; top: 158px; left: 30px; width: 276px; height: 266px; }
  .shutter { position: absolute; bottom: 8px; left: 0; width: 100%; text-align: center; font-size: 11px; color: var(--on-photo); }
  .shutter-button {
    width: 66px; height: 66px; border-radius: 50%; background: var(--paper);
    display: flex; align-items: center; justify-content: center; margin: 0 auto 3px;
  }

  /* result screen */
  .dropdown {
    position: absolute; top: 62px; right: 8px; width: 140px;
    background: var(--brand); color: #fbf1ec; font-size: 12px;
  }
  .dropdown-item { padding: 5px 7px; border-bottom: 1px solid #e8c9b9; white-space: nowrap; }
  .dropdown-item:last-child { border-bottom: none; }
  .email-field { position: absolute; top: 300px; left: 12px; right: 12px; }
  .email-label { font-size: 11px; color: var(--ink); margin-bottom: 6px; white-space: nowrap; }
  .email-input {
    height: 40px; border: 2px solid #bdbdbd; border-radius: 12px; position: relative;
  }
  .email-input::after {
    content: ""; position: absolute; left: 10px; top: 9px; width: 2px; height: 20px; background: #6bb4c8;
  }

  .step-caption {
    position: absolute; top: 920px; width: 360px; text-align: center;
    font-size: 25px; color: var(--ink); line-height: 1.35;
  }
  .step-number { display: block; font-size: 19px; }
  .step-caption--describe { left: 46px; }
  .step-caption--snapshot { left: 420px; }
  .step-caption--result { left: 788px; }
</style>
</head>
<body>
<main class="canvas">
  <h1 class="brand-title">Club Lumora</h1>

  <!-- Step 2: describe and send -->
  <section class="screen screen--describe">
    <header class="app-header">
      <div class="app-name">Club Lumora</div>
      <svg class="menu-icon" viewBox="0 0 20 18"><g fill="var(--brand)"><rect y="0" width="20" height="3"/><rect y="7" width="20" height="3"/><rect y="14" width="20" height="3"/></g></svg>
    </header>
    <nav class="partners"><span>Talvine</span><span>Norelisa</span><span>Parlo</span><span>Ostra</span></nav>
    <div class="describe-photo skin-photo" role="img" aria-label="Close-up photo of the skin area"></div>
    <div class="describe-field">
      <div class="describe-label">Describe and send</div>
      <div class="describe-line"></div>
      <div class="describe-line"></div>
      <div class="describe-line"></div>
      <div class="describe-line"></div>
    </div>
    <div class="actions">
      <div class="action">
        <div class="action-button"><svg width="30" height="30" viewBox="0 0 30 30"><path d="M15 3v24M3 15h24" stroke="#fff" stroke-width="3.5"/></svg></div>New Case
      </div>
      <div class="action">
        <div class="action-button"><svg width="30" height="30" viewBox="0 0 30 30"><path d="M5 16l7 8L26 5" fill="none" stroke="#fff" stroke-width="3.5"/></svg></div>Send
      </div>
    </div>
  </section>

  <!-- Step 1: take a snapshot -->
  <section class="screen screen--snapshot">
    <div class="camera-view skin-photo" role="img" aria-label="Live camera view of skin"></div>
    <header class="app-header">
      <div class="app-name">Club Lumora</div>
      <svg class="menu-icon" viewBox="0 0 20 18"><g fill="#fff"><rect y="0" width="20" height="3"/><rect y="7" width="20" height="3"/><rect y="14" width="20" height="3"/></g></svg>
    </header>
    <nav class="partners"><span>Talvine</span><span>Norelisa</span><span>Parlo</span><span>Ostra</span></nav>
    <svg class="viewfinder" viewBox="0 0 276 266">
      <g fill="none" stroke="#fff" stroke-width="4">
        <path d="M2 52V2h48M226 2h48v50M274 214v50h-48M50 264H2v-50"/>
        <path d="M138 96v72M102 132h72" stroke-width="2"/>
      </g>
    </svg>
    <div class="shutter">
      <div class="shutter-button"><svg width="32" height="26" viewBox="0 0 32 26"><path d="M3 6h7l3-4h6l3 4h7v18H3z" fill="var(--brand)"/><circle cx="16" cy="15" r="6" fill="#fff"/><circle cx="16" cy="15" r="3.5" fill="var(--brand)"/></svg></div>take a Snapshot
    </div>
  </section>

  <!-- Step 3: diagnosis and treatment -->
  <section class="screen screen--result">
    <header class="app-header">
      <div class="app-name">Club Lumora</div>
      <svg class="menu-icon" viewBox="0 0 20 18"><g fill="var(--brand)"><rect y="0" width="20" height="3"/><rect y="7" width="20" height="3"/><rect y="14" width="20" height="3"/></g></svg>
    </header>
    <nav class="dropdown">
      <div class="dropdown-item">Follow up Visit</div>
      <div class="dropdown-item">Rx Refill</div>
      <div class="dropdown-item">Medical Cosmetic Shop</div>
    </nav>
    <div class="email-field">
      <div class="email-label">Type your email to get diagnosis and treatment</div>
      <div class="email-input"></div>
    </div>
    <div class="actions">
      <div class="action">
        <div class="action-button"><svg width="30" height="30" viewBox="0 0 30 30"><path d="M15 3v24M3 15h24" stroke="#fff" stroke-width="3.5"/></svg></div>New Case
      </div>
      <div class="action">
        <div class="action-button"><svg width="30" height="30" viewBox="0 0 30 30"><path d="M5 16l7 8L26 5" fill="none" stroke="#fff" stroke-width="3.5"/></svg></div>Send
      </div>
    </div>
  </section>

  <p class="step-caption step-caption--describe"><span class="step-number">2.</span>Describe and send</p>
  <p class="step-caption step-caption--snapshot"><span class="step-number">1.</span>Take a Snapshop</p>
  <p class="step-caption step-caption--result"><span class="step-number">3.</span>Get diagnosis &amp; treatment</p>
</main>
</body>
</html>
```